Geschäftspapiere für medizinische Schutzausrüstung
Zielgruppe
Medizinische Schutzausrüstung für Deutschland.
Zertifiziert, schnell und unkompliziert.
Für Einrichtungen im Bereich Medizin & Pflege, systemrelevante Industrien sowie für öffentliche Träger.
Aufgabenstellung
Es sollte clean sein, Farben wie , Weiß, blau, grün, wären von Vorteil. Habe keine besondere Vorstellungen lasse mich gerne überraschen.
Siehe .. www.kvoltaq.de

```html
<!DOCTYPE html>
<html lang="de">
<head>
<meta charset="utf-8">
<title>Kvoltaq – Briefbogen</title>
<link href="https://fonts.googleapis.com/css2?family=Lato:wght@400;700&family=Arimo&display=swap" rel="stylesheet">
<style>
  :root {
    --sage: #8aad93;
    --sky: #4fc3ee;
    --sky-soft: #9ad8ee;
    --navy: #17253d;
    --rule: #6b6f80;
    --grey: #555a63;
    --paper: #ffffff;
    --canvas: #ffffff;
    --fold: #2f7fc1;
  }
  * { margin: 0; padding: 0; box-sizing: border-box; }
  html, body { width: 973px; height: 1200px; overflow: hidden; background: var(--canvas); }
  .letterhead {
    position: absolute; left: 136px; top: 25px;
    width: 827px; height: 1170px;
    background: var(--paper);
    font-family: "Lato", sans-serif;
  }
  .band { position: absolute; left: 0; display: block; }
  .band--top { top: 0; }
  .band--bottom { bottom: 9px; }

  .brand {
    position: absolute; right: 54px; top: 120px;
    display: flex; align-items: center; gap: 10px;
    font-family: "Lato", sans-serif; font-weight: 400;
    font-size: 40px; letter-spacing: 6px; color: var(--navy);
  }
  .brand__dot { width: 22px; height: 22px; border-radius: 50%; background: var(--sky); }

  .sender-line {
    position: absolute; left: 86px; top: 210px;
    font-family: "Arimo", sans-serif; font-size: 9.5px; color: var(--grey);
    border-bottom: 1px solid #9aa0a8; padding-bottom: 1px;
  }

  .contact {
    position: absolute; left: 609px; top: 240px;
    border-left: 1.5px solid var(--rule);
    padding-left: 15px; height: 115px;
    color: var(--navy); font-size: 14.5px; line-height: 18px;
    font-style: normal;
  }
  .contact__address { margin-bottom: 8px; }
  .contact__list { list-style: none; }
  .contact__list li { display: flex; align-items: center; gap: 8px; line-height: 19px; }
  .contact__list svg { width: 12px; height: 12px; flex: none; }

  .fold-mark { position: absolute; left: 0; width: 30px; height: 1px; background: var(--fold); }
  .fold-mark--upper { top: 411px; }
  .fold-mark--lower { top: 803px; }

  .legal {
    position: absolute; right: 42px; bottom: 12px;
    display: flex; color: #fff; font-size: 10px; line-height: 12px;
  }
  .legal__group { display: grid; grid-template-columns: auto auto; column-gap: 6px; padding: 0 7px; border-left: 1px solid rgba(255,255,255,.8); }
  .legal__group:first-child { border-left: none; }
</style>
</head>
<body>
<main class="letterhead">
  <svg class="band band--top" width="470" height="22" viewBox="0 0 470 22">
    <defs>
      <linearGradient id="accentTop" x1="0" x2="1" y1="0" y2="0">
        <stop offset="0" stop-color="var(--sky)"/>
        <stop offset="1" stop-color="var(--sky-soft)"/>
      </linearGradient>
    </defs>
    <polygon points="0,0 462,0 445,21 0,21" fill="var(--sage)"/>
    <polygon points="60,0 148,0 131,21 43,21" fill="url(#accentTop)" role="img" aria-label="Dekoratives Akzentfeld in Blau"/>
  </svg>

  <div class="brand"><span class="brand__dot"></span>KVOLTAQ</div>

  <p class="sender-line">Lindmarkweg 12 | 30421 Hannover</p>

  <address class="contact">
    <p class="contact__address">Osterkamp 17<br>31137 Hildesheim</p>
    <ul class="contact__list">
      <li><svg viewBox="0 0 12 12"><path d="M2 1l2 0 1 3-1.5 1a6 6 0 0 0 3.5 3.5L8 7l3 1v2a1 1 0 0 1-1 1A9 9 0 0 1 1 2a1 1 0 0 1 1-1z" fill="var(--sky)"/></svg>040 / 58203917</li>
      <li><svg viewBox="0 0 12 12"><rect x="3" y="1" width="6" height="3" fill="none" stroke="var(--sky)"/><rect x="1" y="4" width="10" height="5" rx="1" fill="none" stroke="var(--sky)"/><rect x="3" y="7" width="6" height="4" fill="#fff" stroke="var(--sky)"/></svg>040 / 58203917</li>
      <li><svg viewBox="0 0 12 12"><circle cx="6" cy="6" r="5" fill="none" stroke="var(--sky)"/><ellipse cx="6" cy="6" rx="2" ry="5" fill="none" stroke="var(--sky)"/><line x1="1" y1="6" x2="11" y2="6" stroke="var(--sky)"/></svg>www.kvoltaq.de</li>
      <li><svg viewBox="0 0 12 12"><rect x="1" y="3" width="10" height="7" fill="var(--sky)"/><path d="M1 3l5 4 5-4" fill="none" stroke="#fff"/></svg>anfrage@kvoltaq.de</li>
    </ul>
  </address>

  <span class="fold-mark fold-mark--upper"></span>
  <span class="fold-mark fold-mark--lower"></span>

  <svg class="band band--bottom" width="827" height="33" viewBox="0 0 827 33">
    <defs>
      <linearGradient id="accentBottom" x1="0" x2="1" y1="0" y2="0">
        <stop offset="0" stop-color="var(--sky)"/>
        <stop offset="1" stop-color="var(--sky-soft)"/>
      </linearGradient>
    </defs>
    <rect x="0" y="0" width="827" height="33" fill="var(--sage)"/>
    <polygon points="56,0 143,0 114,33 27,33" fill="url(#accentBottom)" role="img" aria-label="Dekoratives Akzentfeld in Blau"/>
  </svg>

  <footer class="legal">
    <div class="legal__group"><span>Bank:</span><span>Nordtal Bank eG</span><span></span><span>Hildesheim</span></div>
    <div class="legal__group"><span>USt-IdNr.:</span><span>DE918204576</span><span>Register-Nr.</span><span>HRA 3175</span></div>
    <div class="legal__group"><span>Amtsgericht</span><span>Hildesheim</span><span>Sitz</span><span>Hildesheim</span></div>
    <div class="legal__group"><span>BIC</span><span>NRTLDEF1HIL</span><span>IBAN</span><span>DE47 2804 1927 3305 6182 00</span></div>
  </footer>
</main>
</body>
</html>
```